Business card for a new cabinet shop company named Marlowe Cabinets for high end cabinets

Design a business card, thinking dark rich green with colours to speak of high end luxury ie; cream, gold, black possibly

Peter Lindqvar
Director Craftsman
Email: info@marlowecabinets.com.au
Instagram : @marlowe.cabinets

```html
<!DOCTYPE html>
<html lang="en">
<head>
<meta charset="utf-8">
<title>Marlowe Cabinets – Business Card</title>
<link rel="stylesheet" href="https://fonts.googleapis.com/css2?family=Montserrat:wght@800&family=Open+Sans:wght@400&family=Poppins:wght@400&display=swap">
<style>
  :root {
    --backdrop: #808080;
    --green-deep: #1f5a50;
    --green-shadow: #2b4f4b;
    --green-light: #1b6a5a;
    --gold: #c9a95c;
    --paper: #f1f1f3;
    --ink: #3a3a3c;
    --name-green: #13843f;
    --rule: #c8c8ca;
  }
  * { margin: 0; padding: 0; box-sizing: border-box; }
  html, body {
    width: 1078px;
    height: 1200px;
    overflow: hidden;
    background: var(--backdrop);
  }
  .card {
    position: absolute;
    left: 146px;
    width: 786px;
    height: 448px;
  }
  .card-front {
    top: 133px;
    background:
      radial-gradient(ellipse at 8% 100%, var(--green-light) 0%, transparent 60%),
      linear-gradient(160deg, var(--green-shadow) 0%, var(--green-deep) 45%, #215c52 100%);
    display: flex;
    align-items: center;
    justify-content: center;
  }
  .brand {
    display: flex;
    align-items: center;
    gap: 20px;
  }
  .brand-mark {
    width: 30px;
    height: 30px;
    border-radius: 50%;
    background: var(--gold);
  }
  .brand-name {
    font-family: "Poppins", sans-serif;
    font-weight: 400;
    font-size: 50px;
    letter-spacing: 1px;
    color: var(--gold);
  }
  .card-back {
    top: 632px;
    background: var(--paper);
  }
  .contact {
    position: absolute;
    left: 257px;
    top: 153px;
    width: 272px;
    text-align: center;
    color: var(--ink);
  }
  .contact-name {
    font-family: "Montserrat", sans-serif;
    font-weight: 800;
    font-size: 27px;
    line-height: 32px;
    color: var(--name-green);
    white-space: nowrap;
  }
  .contact-role {
    font-family: "Open Sans", sans-serif;
    font-size: 21px;
    line-height: 30px;
    margin-top: 1px;
    margin-bottom: 6px;
  }
  .contact-social {
    border-top: 1px solid var(--rule);
    border-bottom: 1px solid var(--rule);
    height: 38px;
    display: flex;
    align-items: center;
    justify-content: center;
    gap: 10px;
    font-family: "Open Sans", sans-serif;
    font-size: 23px;
    letter-spacing: 1px;
  }
  .social-dot {
    width: 26px;
    height: 26px;
    border-radius: 50%;
    background: var(--gold);
    flex: none;
  }
  .contact-email {
    font-family: "Open Sans", sans-serif;
    font-size: 18px;
    line-height: 24px;
    margin-top: 8px;
    white-space: nowrap;
    letter-spacing: 0.3px;
  }
</style>
</head>
<body>
  <section class="card card-front">
    <div class="brand">
      <span class="brand-mark"></span>
      <span class="brand-name">Marlowe Cabinets</span>
    </div>
  </section>

  <section class="card card-back">
    <div class="contact">
      <h1 class="contact-name">PETER LINDQVAR</h1>
      <p class="contact-role">Director Craftsman</p>
      <p class="contact-social"><span class="social-dot"></span>@marlowe.cabinets</p>
      <p class="contact-email">info@marlowecabinets.com.au</p>
    </div>
  </section>
</body>
</html>
```